Business card and Stationery for data intelligence company

We need a new design for our business cards and stationery (Business Letter templates and a Quote example on Word, but it MUST work on Google Doc as well).

We are a software company based in Ireland and UK. Our product is "Lumevra", data intelligence platform with beautiful visualizations, graph capabilities (things are interconnected), powerful, flexible, it can manage Big Data and Streaming information. It's modern and relatively open source.
Our company will provide data intelligence for law enforcements, pharmaceuticals, and similar high end customers.

We'll launch a new website soon. At the moment it's http://www.kovar-analytics.example if you want to take a look. This is our youtube channel in case you need it to understand what Lumevra is: https://www.youtube.com/c/kovaranalyticschannel

We changed the logo so please use the logo I attach here.

We'd like the output to be cool and modern but elegant and "business" at the same time. It should inspire simple sophistication, "unity" "intent" "purpose" yet subtly very advanced and innovative.

The name "Lumevra" does NOT refer to sirens (mithological creatures) as well as the warning devices. It means Kinetic Object Vector Analysis Reactor. Please use our logo's colors and if you want to something like the "graph" image.

```html
<!DOCTYPE html>
<html lang="en">
<head>
<meta charset="UTF-8">
<title>Lumevra — Business Card</title>
<link rel="stylesheet" href="https://fonts.googleapis.com/css2?family=Quicksand:wght@500;600;700&display=swap">
<style>
  :root {
    --stage: #ecebe8;
    --card-grey: #808285;
    --brand-orange: #f5ac35;
    --paper-white: #ffffff;
    --ink-light: #ffffff;
    --card-shadow: rgba(0, 0, 0, 0.3);
  }
  * { box-sizing: border-box; margin: 0; padding: 0; }
  html, body {
    width: 1200px; height: 720px; overflow: hidden;
    background: var(--stage);
    font-family: "Quicksand", sans-serif;
  }
  .canvas { position: relative; width: 1200px; height: 720px; }

  .card {
    position: absolute;
    background: var(--card-grey);
    box-shadow: 2px 3px 6px var(--card-shadow);
    overflow: hidden;
  }
  .card--front { left: 109px; top: 116px; width: 487px; height: 292px; }
  .card--back  { left: 622px; top: 307px; width: 508px; height: 307px; }

  .wordmark {
    color: var(--brand-orange);
    font-weight: 600;
    letter-spacing: 3px;
    line-height: 1;
    white-space: nowrap;
  }

  /* Front */
  .front-mark {
    position: absolute; left: 142px; top: 107px;
    width: 79px; height: 79px; border-radius: 50%;
    background: var(--brand-orange);
  }
  .front-pill {
    position: absolute; left: 250px; top: 112px;
    width: 237px; height: 65px;
    background: var(--paper-white);
    border-radius: 16px 0 0 16px;
    display: flex; align-items: center; justify-content: center;
    padding-right: 6px;
  }
  .front-pill .wordmark { font-size: 28px; }

  /* Back */
  .name-tab {
    position: absolute; left: 0; top: 49px;
    width: 245px; height: 78px;
    background: var(--brand-orange);
    border-radius: 0 15px 15px 0;
    padding: 12px 0 0 34px;
    color: var(--ink-light);
  }
  .name-tab__name { font-size: 26px; font-weight: 700; letter-spacing: 1.5px; line-height: 30px; }
  .name-tab__title { font-size: 16px; font-weight: 600; line-height: 20px; }

  .contact-list { position: absolute; left: 32px; top: 0; list-style: none; color: var(--ink-light); }
  .contact-list li {
    position: absolute; left: 0; width: 200px;
    display: flex; align-items: center; gap: 14px;
    font-size: 16.5px; font-weight: 600; letter-spacing: 0.4px;
    height: 24px; white-space: nowrap;
  }
  .contact-list li:nth-child(1) { top: 138px; }
  .contact-list li:nth-child(2) { top: 175px; }
  .contact-list svg { width: 18px; height: 18px; flex: none; }

  .back-brand__mark {
    position: absolute; left: 276px; top: 60px;
    width: 62px; height: 62px; border-radius: 50%;
    background: var(--brand-orange);
  }
  .back-brand__name {
    position: absolute; left: 350px; top: 77px;
    font-size: 27px; letter-spacing: 2px;
  }

  .address-band {
    position: absolute; left: 259px; top: 185px;
    width: 249px; height: 68px;
    background: var(--brand-orange);
    border-radius: 14px 0 0 14px;
    list-style: none; color: var(--ink-light);
  }
  .address-band li {
    position: absolute; left: 28px;
    display: flex; align-items: center; gap: 9px;
    font-size: 16px; font-weight: 600; height: 22px; white-space: nowrap;
  }
  .address-band li:nth-child(1) { top: 8px; }
  .address-band li:nth-child(2) { top: 38px; }
  .address-band svg { width: 18px; height: 18px; flex: none; }
</style>
</head>
<body>
<main class="canvas">

  <section class="card card--front" aria-label="Business card front">
    <div class="front-mark" aria-hidden="true"></div>
    <div class="front-pill">
      <span class="wordmark">LUMEVRA</span>
    </div>
  </section>

  <section class="card card--back" aria-label="Business card back">
    <div class="name-tab">
      <p class="name-tab__name">NAME</p>
      <p class="name-tab__title">Postion/ Title</p>
    </div>

    <ul class="contact-list">
      <li>
        <svg viewBox="0 0 20 20" aria-hidden="true">
          <path d="M2 7 Q10 1 18 7 L16 9 L13 7.5 L13 6 Q10 5 7 6 L7 7.5 L4 9 Z" fill="#fff"/>
          <rect x="4" y="10" width="12" height="8" rx="1.5" fill="#fff"/>
          <circle cx="10" cy="14" r="2" fill="#808285"/>
        </svg>
        Phone number
      </li>
      <li>
        <svg viewBox="0 0 20 20" aria-hidden="true">
          <rect x="5" y="2" width="10" height="16" rx="2" fill="none" stroke="#fff" stroke-width="2"/>
          <line x1="8.5" y1="15" x2="11.5" y2="15" stroke="#fff" stroke-width="1.5"/>
        </svg>
        mobile
      </li>
    </ul>

    <div class="back-brand__mark" aria-hidden="true"></div>
    <span class="wordmark back-brand__name">LUMEVRA</span>

    <ul class="address-band">
      <li>
        <svg viewBox="0 0 20 20" aria-hidden="true" fill="none" stroke="#fff" stroke-width="1.5">
          <circle cx="10" cy="10" r="8"/>
          <ellipse cx="10" cy="10" rx="3.5" ry="8"/>
          <line x1="2" y1="10" x2="18" y2="10"/>
          <line x1="3.5" y1="6" x2="16.5" y2="6"/>
          <line x1="3.5" y1="14" x2="16.5" y2="14"/>
        </svg>
        web address
      </li>
      <li>
        <svg viewBox="0 0 20 20" aria-hidden="true" fill="none" stroke="#fff" stroke-width="1.6" stroke-linejoin="round">
          <path d="M2.5 9.5 L10 3 L17.5 9.5 M4.5 8 V17.5 H8 V12.5 H12 V17.5 H15.5 V8"/>
        </svg>
        physical address
      </li>
    </ul>
  </section>

</main>
</body>
</html>
```